Building technology company seek stationery design and folder design

Letterhead, and a folder design
ideally, I would have two letter head design, one is for one-page bussiness letter. the other one I can use for longer document such report, or analysis regular report page
you can find company logo and overall style at our website:
www.plinthcove.example

we are in building technology business, using internet of things technology to improve building energy efficiency to make building greener.

Industry/Entity Type

It Company

Requirements
Must have
• company logo
Nice to have
• techy look abstract graphics, etc.
Should not have
• no comment

```html
<!DOCTYPE html>
<html lang="en">
<head>
<meta charset="utf-8">
<title>Plinth Cove — Letterhead and Folder</title>
<link href="https://fonts.googleapis.com/css2?family=Michroma&family=Roboto:wght@400&display=swap" rel="stylesheet">
<style>
  :root {
    --backdrop: #dedede;
    --paper: #ffffff;
    --paper-shade: #efefef;
    --brand-green: #a9cf3a;
    --folder-green: #b1d44f;
    --folder-line: #a6c946;
    --ink: #555555;
    --white: #ffffff;
  }
  html, body {
    margin: 0;
    padding: 0;
    width: 1200px;
    height: 821px;
    overflow: hidden;
    background: var(--backdrop);
  }
  .canvas {
    position: relative;
    width: 1200px;
    height: 821px;
  }

  /* Letterhead */
  .letterhead {
    position: absolute;
    left: 74px;
    top: 114px;
    width: 441px;
    height: 622px;
    background: linear-gradient(90deg, var(--paper) 0%, var(--paper-shade) 55%, var(--paper-shade) 100%);
    overflow: hidden;
  }
  .letterhead__circuit {
    position: absolute;
    left: 0;
    top: 0;
    width: 441px;
    height: 230px;
    background:
      repeating-linear-gradient(90deg, rgba(150,220,232,0) 0px, rgba(150,220,232,0) 17px, rgba(150,220,232,0.55) 17px, rgba(150,220,232,0.55) 18px),
      linear-gradient(180deg, rgba(255,255,255,0) 0%, rgba(255,255,255,0) 55%, rgba(255,255,255,1) 100%);
    background-blend-mode: normal;
    -webkit-mask-image: linear-gradient(180deg, #000 0%, #000 55%, transparent 100%);
            mask-image: linear-gradient(180deg, #000 0%, #000 55%, transparent 100%);
  }
  .letterhead__brand {
    position: absolute;
    left: 38px;
    top: 64px;
    width: 114px;
    display: flex;
    flex-direction: column;
    align-items: center;
    gap: 6px;
  }
  .brand-square {
    display: block;
    background: var(--brand-green);
  }
  .letterhead__brand .brand-square {
    width: 20px;
    height: 20px;
  }
  .letterhead__brand-name {
    font-family: "Michroma", sans-serif;
    font-size: 9px;
    letter-spacing: 0.5px;
    color: var(--brand-green);
    white-space: nowrap;
  }
  .letterhead__contact {
    position: absolute;
    left: 314px;
    top: 45px;
    margin: 0;
    padding: 0;
    list-style: none;
    font-family: "Roboto", sans-serif;
    font-size: 6.5px;
    line-height: 9px;
    color: var(--ink);
  }
  .letterhead__contact li {
    display: flex;
    align-items: center;
    gap: 4px;
  }
  .contact-icon {
    width: 6px;
    height: 6px;
    flex: none;
  }
  .letterhead__footer-panel {
    position: absolute;
    left: 0;
    top: 462px;
    width: 441px;
    height: 160px;
    background: linear-gradient(90deg, #f6f6f6 0%, #f1f1f1 100%);
  }
  .letterhead__footer-art {
    position: absolute;
    left: 21px;
    top: 422px;
    width: 374px;
    height: 200px;
    background: linear-gradient(180deg, rgba(169,207,58,0.55) 0%, rgba(169,207,58,0.95) 100%);
  }

  /* Folder */
  .folder {
    position: absolute;
    left: 553px;
    top: 77px;
    width: 519px;
    height: 659px;
    background: var(--folder-green);
    overflow: hidden;
  }
  .folder__circuit {
    position: absolute;
    left: 0;
    top: 0;
    width: 519px;
    height: 280px;
    background: repeating-linear-gradient(90deg, rgba(210,232,140,0) 0px, rgba(210,232,140,0) 20px, rgba(210,232,140,0.7) 20px, rgba(210,232,140,0.7) 21px);
    -webkit-mask-image: linear-gradient(180deg, #000 0%, #000 45%, transparent 100%);
            mask-image: linear-gradient(180deg, #000 0%, #000 45%, transparent 100%);
  }
  .folder__folds {
    position: absolute;
    left: 0;
    top: 0;
    width: 40px;
    height: 659px;
  }
  .folder__brand {
    position: absolute;
    left: 0;
    top: 75px;
    width: 519px;
    display: flex;
    flex-direction: column;
    align-items: center;
    gap: 12px;
  }
  .folder__brand .brand-square {
    width: 64px;
    height: 64px;
    background: var(--white);
  }
  .folder__brand-name {
    font-family: "Michroma", sans-serif;
    font-size: 27px;
    letter-spacing: 1px;
    color: var(--white);
    white-space: nowrap;
  }
</style>
</head>
<body>
<main class="canvas">
  <section class="letterhead" aria-label="Letterhead">
    <div class="letterhead__circuit" role="img" aria-label="Faint cyan circuit-trace pattern running down from the top edge"></div>
    <div class="letterhead__brand">
      <span class="brand-square"></span>
      <span class="letterhead__brand-name">PLINTH COVE</span>
    </div>
    <ul class="letterhead__contact">
      <li>
        <svg class="contact-icon" viewBox="0 0 10 10"><path d="M2 1 L4 1 L5 3 L4 4 Q5 6 6 6 L7 5 L9 6 L9 8 Q8 9 7 9 Q1 8 1 2 Q1 1 2 1Z" fill="var(--brand-green)"/></svg>
        (555) 014-2290
      </li>
      <li>
        <svg class="contact-icon" viewBox="0 0 10 10"><rect x="1" y="2" width="8" height="6" fill="var(--brand-green)"/><path d="M1 2 L5 5.5 L9 2" stroke="#fff" stroke-width="0.8" fill="none"/></svg>
        info@plinthcove.example
      </li>
      <li>
        <svg class="contact-icon" viewBox="0 0 10 10"><circle cx="5" cy="5" r="4" fill="var(--brand-green)"/></svg>
        www.plinthcove.example
      </li>
      <li>
        <svg class="contact-icon" viewBox="0 0 10 10"><circle cx="5" cy="5" r="4" fill="var(--brand-green)"/></svg>
        plinthcove
      </li>
    </ul>
    <div class="letterhead__footer-panel"></div>
    <div class="letterhead__footer-art" role="img" aria-label="Large green brand decoration along the bottom edge of the letterhead"></div>
  </section>

  <section class="folder" aria-label="Presentation folder cover">
    <div class="folder__circuit" role="img" aria-label="Subtle light-green circuit-trace pattern across the top of the cover"></div>
    <svg class="folder__folds" viewBox="0 0 40 659" aria-hidden="true">
      <line x1="8" y1="0" x2="8" y2="659" stroke="var(--folder-line)" stroke-width="1"/>
      <line x1="16" y1="0" x2="16" y2="659" stroke="var(--folder-line)" stroke-width="1"/>
      <line x1="24" y1="0" x2="24" y2="659" stroke="var(--folder-line)" stroke-width="1"/>
      <line x1="31" y1="0" x2="31" y2="659" stroke="var(--folder-line)" stroke-width="1"/>
    </svg>
    <div class="folder__brand">
      <span class="brand-square"></span>
      <span class="folder__brand-name">PLINTH COVE</span>
    </div>
  </section>
</main>
</body>
</html>
```